Quelvane FZE
Engineered for Silence
Quelvane FZE -
Creative Brief
Use specific fonts
Use your own creativity
Professional
T. Orlov
Managing Director & Chief Acoustic Consultant
P.O. Box - 58914, Ras Al Khaimah, U.A.E.
info@quelvane-example.com
www.quelvane-example.com
Please provide Business card, letter head, quotation, invoice, fax & envelop designs
Services & Products: Acoustic Consultants, Acoustic Contracting, Acoustic Spray, Acoustic Underlay, Load Bearing Pads, Acoustic Louvers, Sound Attenuators, Inertia Bases, Floating Floors, Acoustic Doors, Acoustic Barriers, Acoustic Enclosure, Generator Enclosure, Sand Trap Louvers, Extract Louvers, MEP Contracting

```html
<!DOCTYPE html>
<html lang="en">
<head>
<meta charset="utf-8">
<title>Quelvane FZE — Stationery Set</title>
<link rel="stylesheet" href="https://fonts.googleapis.com/css2?family=Open+Sans:wght@400;700&display=swap">
<style>
  :root {
    --brand-blue: #1f5a9e;
    --brand-green: #5ea83d;
    --paper: #ffffff;
    --ink-grey: #8a8f94;
    --ink-dark: #5a5f64;
    --rule-grey: #c9cdd1;
    --card-dark: #5c6166;
    --card-mid: #9a9ea2;
    --stage: #ffffff;
  }
  * { box-sizing: border-box; margin: 0; padding: 0; }
  html, body { width: 1200px; height: 394px; overflow: hidden; background: var(--stage); }
  body { position: relative; font-family: "Open Sans", Arial, sans-serif; color: var(--ink-grey); }

  .sheet {
    position: absolute;
    background: var(--paper);
    box-shadow: 0 3px 6px rgba(0,0,0,0.18), 0 0 1px rgba(0,0,0,0.15);
    overflow: hidden;
  }

  .brand { display: inline-flex; align-items: center; gap: 3px; white-space: nowrap; }
  .brand-dot { width: 12px; height: 12px; border-radius: 50%; background: var(--brand-green); flex: none; }
  .brand-name { font-weight: 700; font-size: 9px; color: var(--brand-blue); letter-spacing: -0.1px; }

  .footer-rule { position: absolute; left: 10px; right: 10px; bottom: 14px; height: 1px; background: var(--brand-green); }
  .footer-text { position: absolute; left: 10px; right: 10px; bottom: 6px; font-size: 3.4px; color: var(--ink-grey); white-space: nowrap; }

  .doc-title { position: absolute; right: 12px; font-size: 15px; font-weight: 400; color: var(--ink-grey); letter-spacing: 1px; }

  /* Shared field grid (fax, quotation, invoice) */
  .field-grid { position: absolute; left: 12px; right: 12px; display: grid; grid-template-columns: 1fr 1fr; column-gap: 10px; row-gap: 6px; }
  .field { display: flex; align-items: flex-end; font-size: 4.5px; height: 12px; border-bottom: 1px solid var(--rule-grey); white-space: nowrap; }

  /* Item table (quotation, invoice) */
  .item-table { position: absolute; left: 12px; right: 12px; border-collapse: collapse; font-size: 4.2px; }
  .item-table th { background: var(--brand-blue); color: #fff; font-weight: 700; text-align: left; padding: 2px 3px; }
  .item-table td { height: 11px; border-bottom: 1px solid var(--rule-grey); padding: 0 3px; }
  .item-table .num { text-align: right; width: 18%; }
  .item-table .qty { text-align: right; width: 10%; }
  .totals { position: absolute; right: 12px; width: 80px; font-size: 4.5px; }
  .totals p { display: flex; justify-content: space-between; border-bottom: 1px solid var(--rule-grey); padding: 2px 0; }
  .totals .grand { color: var(--brand-blue); font-weight: 700; }

  /* Quotation */
  .quotation { left: 5px; top: 12px; width: 259px; height: 348px; }
  .quotation .brand { position: absolute; right: 12px; top: 14px; }
  .quotation .header-rule { position: absolute; left: 10px; right: 10px; top: 38px; height: 1px; background: var(--rule-grey); }
  .quotation .doc-title { top: 50px; }
  .quotation .field-grid { top: 76px; }
  .quotation .item-table { top: 120px; }
  .quotation .totals { top: 228px; }

  /* Fax */
  .fax { left: 276px; top: 12px; width: 257px; height: 348px; }
  .fax .brand { position: absolute; left: 9px; top: 14px; }
  .fax .header-contact { position: absolute; right: 10px; top: 22px; font-size: 4px; }
  .fax .header-rule { position: absolute; left: 9px; right: 9px; top: 34px; height: 1px; background: var(--brand-green); }
  .fax .doc-title { top: 116px; }
  .fax .field-grid { top: 140px; }
  .fax-options { position: absolute; left: 12px; right: 12px; top: 236px; display: flex; justify-content: space-between; font-size: 4.2px; }
  .fax-option { display: flex; align-items: center; gap: 2px; }
  .fax-option::before { content: ""; width: 5px; height: 5px; border: 1px solid var(--ink-grey); }
  .fax-comments { position: absolute; left: 12px; top: 252px; font-size: 4.5px; }

  /* Envelope back */
  .envelope-back { left: 540px; top: 6px; width: 264px; height: 90px; }
  .envelope-back svg { display: block; }

  /* Envelope front */
  .envelope-front { left: 540px; top: 104px; width: 264px; height: 128px; }
  .envelope-front .brand { position: absolute; left: 12px; top: 14px; }
  .envelope-front .header-rule { position: absolute; left: 12px; right: 12px; top: 34px; height: 1px; background: var(--brand-green); }
  .envelope-front .return-line { position: absolute; right: 12px; top: 27px; font-size: 3.6px; }

  /* Compliment slip */
  .slip-map { left: 540px; top: 240px; width: 264px; height: 120px; }
  .slip-map .brand { position: absolute; left: 12px; top: 10px; }
  .slip-map .map-area { position: absolute; left: 0; right: 0; top: 30px; bottom: 0;
    background: radial-gradient(ellipse at 50% 70%, #d9dcdf 0%, #eceef0 60%, #f6f7f8 100%); }

  /* Invoice */
  .invoice { left: 816px; top: 12px; width: 257px; height: 348px; }
  .invoice .brand { position: absolute; right: 12px; top: 14px; }
  .invoice .header-rule { position: absolute; left: 10px; right: 10px; top: 38px; height: 1px; background: var(--rule-grey); }
  .invoice .map-area { position: absolute; left: 6px; right: 6px; top: 70px; height: 220px;
    background: radial-gradient(ellipse at 55% 50%, #eef0f1 0%, #f4f5f6 55%, #ffffff 100%); }
  .invoice .doc-title { top: 50px; }
  .invoice .field-grid { top: 76px; }
  .invoice .item-table { top: 120px; }
  .invoice .totals { top: 228px; }

  /* Business cards */
  .card { width: 96px; height: 58px; }
  .card-front { left: 1092px; top: 12px; }
  .card-front .brand { position: absolute; right: 6px; top: 6px; }
  .card-front .brand-name { font-size: 6px; }
  .card-front .brand-dot { width: 8px; height: 8px; }
  .card-person { position: absolute; left: 6px; top: 21px; line-height: 1.25; }
  .card-person .person-name { font-size: 4.6px; font-weight: 700; color: var(--brand-blue); }
  .card-person .person-title { font-size: 2.6px; color: var(--ink-grey); }
  .card-front .card-rule { position: absolute; left: 6px; right: 6px; top: 36px; height: 1px; background: var(--brand-green); }
  .card-contact { position: absolute; left: 6px; right: 6px; top: 39px; font-size: 2.7px; line-height: 1.35; color: var(--ink-dark); white-space: nowrap; }
  .card-dark { left: 1092px; top: 80px; background: linear-gradient(160deg, #6b7075, var(--card-dark)); }
  .card-mid { left: 1092px; top: 146px; background: linear-gradient(160deg, #b2b5b8, var(--card-mid)); }
  .card-dark .brand, .card-mid .brand { position: absolute; right: 8px; top: 8px; }
  .card-dark .brand-name, .card-mid .brand-name { font-size: 6px; color: #ffffff; }
  .card-dark .brand-dot, .card-mid .brand-dot { width: 8px; height: 8px; }
  .card-vertical { left: 1122px; top: 232px; width: 56px; height: 96px; }
  .card-vertical .brand { position: absolute; left: 0; right: 0; top: 40px; flex-direction: column; gap: 2px; }
  .card-vertical .brand-name { font-size: 5.5px; }
  .card-vertical .brand-dot { width: 14px; height: 14px; }
  .card-vertical .card-web { position: absolute; left: 0; right: 0; bottom: 8px; text-align: center; font-size: 2.8px; }
</style>
</head>
<body>

  <section class="sheet quotation" aria-label="Quotation">
    <div class="brand"><span class="brand-dot"></span><span class="brand-name">Quelvane FZE</span></div>
    <div class="header-rule"></div>
    <h2 class="doc-title">QUOTATION</h2>
    <div class="field-grid">
      <div class="field">Quotation No:</div><div class="field">Date:</div>
      <div class="field">Client:</div><div class="field">Project:</div>
    </div>
    <table class="item-table">
      <thead><tr><th>Description</th><th class="qty">Qty</th><th class="num">Rate</th><th class="num">Amount</th></tr></thead>
      <tbody>
        <tr><td></td><td></td><td></td><td></td></tr><tr><td></td><td></td><td></td><td></td></tr>
        <tr><td></td><td></td><td></td><td></td></tr><tr><td></td><td></td><td></td><td></td></tr>
        <tr><td></td><td></td><td></td><td></td></tr><tr><td></td><td></td><td></td><td></td></tr>
      </tbody>
    </table>
    <div class="totals">
      <p><span>Subtotal</span><span></span></p>
      <p><span>VAT</span><span></span></p>
      <p class="grand"><span>Total</span><span></span></p>
    </div>
    <div class="footer-rule"></div>
    <p class="footer-text">P.O. Box - 58914, Ras Al Khaimah, U.A.E. &nbsp;|&nbsp; info@quelvane-example.com &nbsp;|&nbsp; www.quelvane-example.com</p>
  </section>

  <section class="sheet fax" aria-label="Fax sheet">
    <div class="brand"><span class="brand-dot"></span><span class="brand-name">Quelvane FZE</span></div>
    <p class="header-contact">www.quelvane-example.com</p>
    <div class="header-rule"></div>
    <h2 class="doc-title">FAX</h2>
    <div class="field-grid">
      <div class="field">To:</div><div class="field">From:</div>
      <div class="field">Fax:</div><div class="field">Pages:</div>
      <div class="field">Phone:</div><div class="field">Date:</div>
      <div class="field">Re:</div><div class="field">CC:</div>
    </div>
    <div class="fax-options">
      <span class="fax-option">Urgent</span>
      <span class="fax-option">For Review</span>
      <span class="fax-option">Please Comment</span>
      <span class="fax-option">Please Reply</span>
      <span class="fax-option">Please Recycle</span>
    </div>
    <p class="fax-comments">Comments:</p>
    <div class="footer-rule"></div>
    <p class="footer-text">P.O. Box - 58914, Ras Al Khaimah, U.A.E. &nbsp;|&nbsp; info@quelvane-example.com &nbsp;|&nbsp; www.quelvane-example.com</p>
  </section>

  <section class="sheet envelope-back" aria-label="Envelope back">
    <svg width="264" height="90" viewBox="0 0 264 90">
      <defs>
        <linearGradient id="flap" x1="0" y1="0" x2="0" y2="1">
          <stop offset="0" stop-color="#5d6267"/>
          <stop offset="1" stop-color="#9ea2a6"/>
        </linearGradient>
      </defs>
      <rect width="264" height="90" fill="#d4d7da"/>
      <polygon points="0,0 264,0 132,62" fill="url(#flap)"/>
      <circle cx="132" cy="48" r="9" fill="#5ea83d"/>
    </svg>
  </section>

  <section class="sheet envelope-front" aria-label="Envelope front">
    <div class="brand"><span class="brand-dot"></span><span class="brand-name">Quelvane FZE</span></div>
    <p class="return-line">www.quelvane-example.com</p>
    <div class="header-rule"></div>
  </section>

  <section class="sheet slip-map" aria-label="Compliment slip">
    <div class="map-area" role="img" aria-label="Faint grey world map background"></div>
  </section>

  <section class="sheet invoice" aria-label="Invoice">
    <div class="brand"><span class="brand-dot"></span><span class="brand-name">Quelvane FZE</span></div>
    <div class="header-rule"></div>
    <div class="map-area" role="img" aria-label="Faint grey world map watermark"></div>
    <h2 class="doc-title">INVOICE</h2>
    <div class="field-grid">
      <div class="field">Invoice No:</div><div class="field">Date:</div>
      <div class="field">Bill To:</div><div class="field">Due Date:</div>
    </div>
    <table class="item-table">
      <thead><tr><th>Description</th><th class="qty">Qty</th><th class="num">Rate</th><th class="num">Amount</th></tr></thead>
      <tbody>
        <tr><td></td><td></td><td></td><td></td></tr><tr><td></td><td></td><td></td><td></td></tr>
        <tr><td></td><td></td><td></td><td></td></tr><tr><td></td><td></td><td></td><td></td></tr>
        <tr><td></td><td></td><td></td><td></td></tr><tr><td></td><td></td><td></td><td></td></tr>
      </tbody>
    </table>
    <div class="totals">
      <p><span>Subtotal</span><span></span></p>
      <p><span>VAT</span><span></span></p>
      <p class="grand"><span>Total Due</span><span></span></p>
    </div>
    <div class="footer-rule"></div>
    <p class="footer-text">P.O. Box - 58914, Ras Al Khaimah, U.A.E. &nbsp;|&nbsp; info@quelvane-example.com &nbsp;|&nbsp; www.quelvane-example.com</p>
  </section>

  <section class="sheet card card-front" aria-label="Business card front">
    <div class="brand"><span class="brand-dot"></span><span class="brand-name">Quelvane FZE</span></div>
    <div class="card-person">
      <p class="person-name">T. Orlov</p>
      <p class="person-title">Managing Director &amp; Chief Acoustic Consultant</p>
    </div>
    <div class="card-rule"></div>
    <div class="card-contact">
      <p>P.O. Box - 58914, Ras Al Khaimah, U.A.E.</p>
      <p>info@quelvane-example.com</p>
      <p>www.quelvane-example.com</p>
    </div>
  </section>

  <section class="sheet card card-dark" aria-label="Business card back, dark">
    <div class="brand"><span class="brand-dot"></span><span class="brand-name">Quelvane FZE</span></div>
  </section>

  <section class="sheet card card-mid" aria-label="Business card back, grey">
    <div class="brand"><span class="brand-dot"></span><span class="brand-name">Quelvane FZE</span></div>
  </section>

  <section class="sheet card-vertical" aria-label="Vertical business card">
    <div class="brand"><span class="brand-dot"></span><span class="brand-name">Quelvane FZE</span></div>
    <p class="card-web">www.quelvane-example.com</p>
  </section>

</body>
</html>
```